The Marisol & Jocelyn Fruit Co.

We produce a very high quality freeze dried fruit, all organic, no preservative, no additives, nothing but the fruit. To get more use out of a facility we have in Charlotte, we decided to pursue some high end online retailers with a high end freeze dried organic fruit. We are looking for a very high end, upper east side, trendy, hip, logo and package design for this. There are 4 SKU's - Freeze Dried Strawberries, Freeze Dried Blueberries, Freeze Dried Cherries, and a blend of of all 3 as the 4th SKU. 2 labels each that are 6" x 6" - The front, again needs to be fun and trendy big bold etc. Nothing frilly and Quiet Barn by the creek. The back needs to contain the nutritional statements for each and some copy describing the product and the company.
Updates
This would be one of only a few competitors in this segment
We are looking to steal a page from the wine industry. The coolest looking label on the shelf wins over the uneducated wine buyer. The designs are all fine, but they need to be sleeker, sexier, funner, etc. Someone should look at the label and say....wow that is FUN AND SEXY! I have to buy some! VORBEX.COM screams that. Don't worry so much about pictures of the fruit as the bag is going to be clear. Sell the brand not the fruit. OK?
Reason: Why not?
Reason: Final Selection by Monday 5pm EST.
For all designs that have not been eliminated:
Reason: Final selections. All four designs front and back on one file uploaded by noon tomorrow ( 12:01 PM EST New York)
Target Market(s)
People that would shop at sites like www.vorbex.com
Industry/Entity Type
It Company
Requirements
Nice to have
- The brand is named after our two daughters - One is very girly and the other is very "sassy" It would be fun to have the logo capture their personalities a little. I have uploaded a picture. Marisol on the left, Jocelyn on the right.
Also, another of our brands, Hank Pellow, packaging is attached here. Some consistency in look and feel may be good.
Should not have
- Nothing frilly or dainty, or delicate. Colorful fun and bold but trendy.

```html
<!DOCTYPE html>
<html lang="en">
<head>
<meta charset="utf-8">
<title>Marisol &amp; Jocelyn Fruit Co – Back Label</title>
<link href="https://fonts.googleapis.com/css2?family=Archivo+Black&family=Archivo+Narrow:ital,wght@0,400;0,700;1,400&family=Poiret+One&family=Great+Vibes&display=swap" rel="stylesheet">
<style>
  :root{
    --berry:#9c2620;
    --berry-light:#c22a2e;
    --berry-deep:#8f1b1c;
    --cream:#ffffff;
    --frame:#ffd75c;
    --ink:#141414;
    --rule:#9a9a9a;
  }
  *{margin:0;padding:0;box-sizing:border-box}
  html,body{width:1200px;height:1200px;overflow:hidden;background:var(--berry)}
  .label{position:relative;width:1200px;height:1200px;background:var(--berry);overflow:hidden;color:var(--cream)}

  .fruit-art{position:absolute;left:-330px;top:260px;width:960px;height:1000px;border-radius:48% 52% 46% 54%/40% 40% 60% 60%;
    background:radial-gradient(ellipse at 45% 35%,#d23a3c 0%,var(--berry-light) 40%,var(--berry-deep) 80%,rgba(143,27,28,0) 100%);}

  .brand{position:absolute;left:60px;top:76px;width:380px;text-align:center;font-family:"Poiret One",sans-serif;color:var(--cream);line-height:1}
  .brand .brand-main{font-size:60px;display:block;line-height:62px}
  .brand .brand-sub{font-size:30px;letter-spacing:3px;display:block;margin-top:10px}

  .promise{position:absolute;left:60px;top:270px;width:370px;text-align:center;font-family:"Poiret One",sans-serif;font-size:30px;line-height:46px}

  .slogan{position:absolute;left:44px;top:410px;width:410px;height:240px;font-family:"Great Vibes",cursive;color:var(--cream)}
  .slogan .big{position:absolute;font-size:84px;line-height:1;white-space:nowrap}
  .slogan .nothing{left:0;top:10px}
  .slogan .fruit{left:226px;top:132px}
  .slogan .small{position:absolute;left:56px;top:118px;font-family:"Poiret One",sans-serif;font-size:50px;line-height:1;white-space:nowrap}

  .story{position:absolute;left:46px;top:678px;width:399px;font-family:"Poiret One",sans-serif;font-size:22.5px;line-height:33.4px}
  .story span{display:block;white-space:nowrap;text-align:justify;text-align-last:justify}

  .facts-frame{position:absolute;left:466px;top:74px;width:690px;height:1042px;background:var(--frame);padding:14px}
  .facts{width:100%;height:100%;background:#fff;border:3px solid var(--ink);padding:4px 22px 0 20px;color:var(--ink);font-family:"Archivo Narrow",sans-serif;overflow:hidden}
  .facts h1{font-family:"Archivo Black",sans-serif;font-size:70px;line-height:72px;height:72px;white-space:nowrap}
  .serving{font-size:37px;line-height:44px}
  .bar-thick{height:36px;background:var(--ink);margin-top:12px}
  .bar-mid{height:16px;background:var(--ink)}
  .row{display:flex;justify-content:space-between;align-items:center;border-bottom:2px solid var(--rule);font-size:37px;height:53.5px;white-space:nowrap}
  .row b{font-family:"Archivo Black",sans-serif;font-weight:400;font-size:35px}
  .row.indent{padding-left:22px}
  .row.small-head{font-family:"Archivo Black",sans-serif;font-size:27px;height:44px}
  .row.dv{justify-content:flex-end}
  .row .pct{font-family:"Archivo Black",sans-serif;font-size:35px}
  .row.no-rule{border-bottom:none}
  .row.calories{height:50px}
  .bar-protein{height:34px;background:var(--ink)}
  .vitamins .row{height:47px}
  .vit{display:grid;grid-template-columns:205px 93px 50px 1fr auto;align-items:center;width:100%}
  .dot{text-align:center;font-size:28px}
  .footnote{font-size:24px;line-height:32px;letter-spacing:-.3px;white-space:nowrap}
</style>
</head>
<body>
<main class="label">
  <div class="fruit-art" role="img" aria-label="Large strawberry illustration in soft red tones"></div>

  <div class="brand">
    <span class="brand-main">Marisol &amp;<br>Jocelyn</span>
    <span class="brand-sub">FRUIT CO</span>
  </div>

  <p class="promise">all organic,<br>no preservatives,<br>no additives,</p>

  <div class="slogan">
    <span class="big nothing">Nothing</span>
    <span class="small">but the</span>
    <span class="big fruit">Fruit</span>
  </div>

  <p class="story">
    <span>At vero eos et accusam et justo duo</span>
    <span>dolores et ea rebum. Stet clita kasd</span>
    <span>gubergren, no sea takimata sanctus</span>
    <span>est Lorem ipsum dolor sit. Duis autem</span>
    <span>vel eum iriure dolor in hendrerit in</span>
    <span>vulputate velit esse molestie consequat,</span>
    <span>illum dolore eu feugiat nulla facilisis at</span>
    <span>vero eros et accumsan et iusto odio</span>
    <span>dignissim qui blandit praesent luptatum</span>
    <span>zzril delenit augue duis dolore te</span>
    <span>feugait nulla facilisi. Stet clita kasd</span>
    <span>gubergren, no sea takimata sanctus</span>
    <span>est Lorem ipsum dolor sit. Duis autem</span>
  </p>

  <section class="facts-frame">
    <div class="facts">
      <h1>Nutrition Facts</h1>
      <p class="serving">Serving Size 1/4 cup (6g)<br>Servings Per Container 1.5</p>
      <div class="bar-thick"></div>
      <div class="row small-head">Amount Per Serving</div>
      <div class="row calories no-rule"><span><b>Calories</b> 20</span><span>Calories from Fat 0</span></div>
      <div class="bar-mid"></div>
      <div class="row small-head dv">% Daily Value*</div>
      <div class="row"><span><b>Total Fat</b>&nbsp; 0g</span><span class="pct">0%</span></div>
      <div class="row indent"><span>Saturated Fat&nbsp; 0g</span><span class="pct">0%</span></div>
      <div class="row indent"><span><i>Trans</i> Fat&nbsp; 0g</span></div>
      <div class="row"><span><b>Cholesterol</b>&nbsp; 0mg</span><span class="pct">0%</span></div>
      <div class="row"><span><b>Sodium</b>&nbsp; 0mg</span><span class="pct">0%</span></div>
      <div class="row"><span><b>Total Carbohydrate</b>&nbsp; 5g</span><span class="pct">2%</span></div>
      <div class="row indent"><span>Dietary Fiber&nbsp; 1g</span><span class="pct">4%</span></div>
      <div class="row indent"><span>Sugars&nbsp; 3g</span></div>
      <div class="row no-rule"><span><b>Protein</b>&nbsp; 0g</span></div>
      <div class="bar-protein"></div>
      <div class="vitamins">
        <div class="row"><div class="vit"><span>Vitamin A</span><span>0%</span><span class="dot">•</span><span>Vitamin C</span><span>60%</span></div></div>
        <div class="row"><div class="vit"><span>Calcium</span><span>0%</span><span class="dot">•</span><span>Iron</span><span>2%</span></div></div>
      </div>
      <p class="footnote">*Percent Daily Values are based on a 2,000 calorie diet.</p>
    </div>
  </section>
</main>
</body>
</html>
```